single page with calendar booking ability

a single web page that has the ability to book calendar times and dates, also needs to be able to link to my other business social media seamlessly. I don't want to get multiple developers and or agency's involved, I want you the web designer to design it and make sure it's up and works as described
. The boats we work on are between 20 feet to 40 feet, bow riders , cabin cruisers, and center consoles. The brands that we work on include but are not limited to Halvenk, Trindle, Pike dorrel, Oro vane, Quillard, Brevik, Talvo, and many more. Winterization and shrink wrapping is completely different than graphic wrapping, we do not do graphic's wrapping. Also, only 5% of our business will be auto detailing, the rest will be boats on trailers. Please ensure that the calendar booking system is intergraded and not a surprise to me later

Target Market(s)

Lakes region New Hampshire

Industry/Entity Type

marine

Coding

Coded - Design and coding required

Number of Pages Required

1 page

Colors
0054AA
0677BA
7BADD7
CADEEF
E8F1F8
00AB8E
00BBA5
67D7C9
C6EFE9
E9F9F6
EE7325
F08F49
F5BC92
FAE3D3
FDF4ED

Requirements
Must have
• calendar booking capability
Nice to have
• Pictures of boats being shrink wrapped for the winter season, Nice before and after pictures of boats detailed, only 5% of our business is auto detailing
Should not have
• Large yachts, lots of sail boats as we only do a few, graphics wrapping.. we don't graphic wrap

```html
<!DOCTYPE html>
<html lang="en">
<head>
<meta charset="utf-8">
<title>Harbor Peak Marine &amp; Auto</title>
<link href="https://fonts.googleapis.com/css2?family=Roboto:wght@400;500;700;900&family=Russo+One&display=swap" rel="stylesheet">
<style>
:root{
  --blue:#0677BA;
  --blue-bright:#1A7FD0;
  --blue-deep:#0054AA;
  --blue-soft:#7BADD7;
  --blue-pale:#CADEEF;
  --ink:#111;
  --text:#333;
  --muted:#555;
  --grey-bg:#F4F4F4;
  --white:#fff;
  --footer:#0B0B0B;
}
*{box-sizing:border-box;margin:0;padding:0}
html,body{width:1200px;height:4769px;overflow:hidden}
body{font-family:'Roboto',sans-serif;color:var(--text);background:var(--white)}
.page{position:relative;width:1200px;height:4769px;overflow:hidden}
section{position:absolute;left:0;width:1200px}
.display{font-family:'Russo One',sans-serif;color:var(--ink);text-transform:uppercase}
.center{text-align:center}
.arrow{position:absolute}

/* hero */
.hero{top:0;height:626px}
.hero-photo{position:absolute;inset:0;background:
  radial-gradient(ellipse 620px 200px at 640px 330px,rgba(235,165,95,.7),rgba(235,165,95,0) 70%),
  linear-gradient(180deg,#5d6a78 0%,#858a91 32%,#b39173 52%,#5e4c42 66%,#2e2a28 82%,#1b1a1a 100%)}
.brand{position:absolute;left:100px;top:28px;color:var(--white);font-weight:900;font-size:21px;line-height:22px;letter-spacing:.5px}
.call{position:absolute;left:538px;top:20px;display:flex;align-items:center;gap:8px;color:var(--white)}
.call .ico{width:32px;height:32px;border-radius:50%;background:var(--blue-bright);display:flex;align-items:center;justify-content:center}
.call small{display:block;font-size:10px}
.call strong{display:block;font-size:15px;font-weight:500}
.search{position:absolute;left:689px;top:18px;width:189px;height:34px;border-radius:17px;background:var(--white);font-size:11px;color:#555;padding:10px 16px}
.search svg{position:absolute;right:12px;top:9px}
.btn{display:inline-flex;align-items:center;justify-content:center;background:var(--blue-bright);color:var(--white);font-weight:700;border-radius:22px;text-transform:uppercase}
.book-top{position:absolute;left:889px;top:18px;width:209px;height:34px;font-size:12px}
.nav{position:absolute;top:75px;left:0;width:1200px;height:18px;font-size:14px;color:var(--white)}
.nav span{position:absolute}
.hero-title{position:absolute;left:115px;top:222px;color:var(--white);font-family:'Russo One',sans-serif;font-size:62px;line-height:64px}
.hero-sub-title{position:absolute;left:115px;top:284px;color:var(--white);font-family:'Russo One',sans-serif;font-size:34px}
.hero-lead{position:absolute;left:115px;top:337px;width:350px;color:var(--white);font-size:17px;line-height:24px}
.quote{position:absolute;left:115px;top:407px;width:163px;height:43px;font-size:13px}
.dots{position:absolute;top:572px;left:554px;display:flex;gap:13px}
.dots i{display:block;width:12px;height:12px;border:1.5px solid var(--white);border-radius:50%}
.dots i.on{background:var(--white)}

/* mission */
.mission{top:626px;height:350px}
.mission h2{position:absolute;top:84px;width:100%;font-size:38px}
.mission .lead{position:absolute;top:140px;left:190px;width:820px;font-weight:700;font-size:17px;line-height:28px;color:var(--ink)}
.mission p.body{position:absolute;top:205px;left:190px;width:820px;font-size:15px;line-height:29px;color:var(--text)}

/* services */
.services{top:976px;height:554px;background:var(--grey-bg)}
.services h2{position:absolute;top:68px;width:100%;font-size:32px}
.svc{position:absolute;top:128px;width:242px;height:354px;background:var(--white)}
.svc .ph{height:167px}
.svc .badge{position:absolute;left:91px;top:137px;width:60px;height:60px;border-radius:50%;background:var(--blue-bright);display:flex;align-items:center;justify-content:center}
.svc h3{position:absolute;top:204px;width:100%;text-align:center;font-size:15px;font-weight:700;color:var(--ink)}
.svc .price{position:absolute;top:232px;width:100%;text-align:center;font-size:14px;color:var(--blue)}
.svc p{position:absolute;top:258px;left:18px;width:206px;text-align:center;font-size:11px;line-height:18px;color:var(--muted)}
.svc .book{position:absolute;top:307px;left:47px;width:148px;height:34px;border:1.5px solid var(--blue-bright);border-radius:17px;color:var(--blue);font-size:12px;font-weight:700;display:flex;align-items:center;justify-content:center}

/* stats */
.stats{top:1530px;height:563px;background:
  radial-gradient(ellipse 600px 160px at 600px 330px,rgba(255,255,255,.18),rgba(255,255,255,0) 70%),
  linear-gradient(180deg,#0b6eb8,#1480c6 45%,#0d6db4)}
.stats h2{position:absolute;top:72px;left:222px;width:756px;color:var(--white);font-size:19px;line-height:31px}
.stat{position:absolute;top:202px;width:296px;height:296px;border-radius:50%;background:rgba(255,255,255,.22)}
.stat .in{position:absolute;left:13px;top:13px;width:270px;height:270px;border-radius:50%;background:var(--white);text-align:center}
.stat svg{margin-top:46px}
.stat .val{font-size:40px;font-weight:500;color:var(--blue);margin-top:8px;line-height:46px}
.stat .lbl{font-size:15px;line-height:23px;color:#333;width:190px;margin:6px auto 0}

/* uniqueness */
.unique{top:2093px;height:741px;background:var(--grey-bg)}
.unique h2{position:absolute;top:82px;left:100px;width:1000px;font-size:20px;line-height:35px;font-weight:500;color:var(--ink);text-transform:uppercase}
.big{position:absolute;font-family:'Russo One',sans-serif;font-size:250px;line-height:190px;color:var(--blue-bright);height:190px;overflow:hidden}
.sw{position:absolute;width:381px;height:198px;background:var(--white);border-right:3px solid var(--blue-bright);border-bottom:3px solid var(--blue-bright);padding:28px 24px 0 24px}
.sw h3{font-size:20px;font-weight:400;color:var(--ink);margin-bottom:12px}
.sw p{font-size:13px;line-height:26px;color:#333}
.sw .ic{position:absolute;right:-26px;top:-26px;width:54px;height:54px;border-radius:50%;background:var(--white);border:2px solid var(--blue-bright);display:flex;align-items:center;justify-content:center}

/* calendar */
.calendar{top:2834px;height:790px}
.cal-band{position:absolute;left:0;top:0;width:1200px;height:528px;background:linear-gradient(180deg,#0e78c4,#1487cf 50%,#0b6fb8)}
.calendar h2{position:absolute;top:64px;width:100%;color:var(--white);font-size:34px}
.calendar .intro{position:absolute;top:120px;left:250px;width:700px;color:var(--white);font-size:16px;line-height:27px}
.cal-card{position:absolute;left:194px;top:199px;width:812px;height:424px;background:var(--white);box-shadow:0 2px 8px rgba(0,0,0,.15)}
.cal-left{position:absolute;left:0;top:0;width:573px;height:424px;background:#EEEEEE}
.month{position:absolute;top:58px;width:573px;text-align:center;font-size:16px;color:var(--ink)}
.grid{position:absolute;left:38px;top:100px;display:grid;grid-template-columns:repeat(7,73px);grid-auto-rows:36px;font-size:12px;color:#222;text-align:center;align-items:center;justify-items:center}
.grid .h{font-size:14px}
.grid .d{width:24px;height:24px;line-height:24px;border-radius:50%}
.grid .d.on{background:var(--blue-bright);color:var(--white)}
.sched{position:absolute;left:60px;top:328px;width:250px;height:37px;font-size:13px}
.cal-brand{position:absolute;left:573px;top:58px;width:239px;text-align:center;color:var(--blue-deep);font-weight:900;font-size:20px;line-height:22px}
.event{position:absolute;left:610px;width:190px}
.event .t{display:flex;align-items:center;gap:6px;font-size:11px;font-weight:700;color:var(--ink)}
.event .t b{width:26px;height:26px;border-radius:50%;background:var(--blue-bright);color:var(--white);font-size:11px;display:flex;align-items:center;justify-content:center}
.event p{font-size:9px;line-height:14px;color:#555;margin-top:4px}
.event hr{border:0;border-top:1px solid #ddd;margin-top:10px}

/* news */
.news{top:3622px;height:430px}
.news h2{position:absolute;top:-74px;width:100%;font-size:36px}
.post{position:absolute;top:0;width:318px;height:408px;background:var(--white);border:1px solid #eee;box-shadow:0 1px 6px rgba(0,0,0,.08)}
.post .ph{height:215px}
.post .date{position:absolute;left:11px;width:37px;height:44px;background:var(--blue-bright);color:var(--white);text-align:center;font-size:16px;font-weight:500;line-height:18px;padding-top:5px}
.post .date small{display:block;font-size:10px}
.post h3{margin-top:20px;text-align:center;font-size:19px;font-weight:700;color:var(--ink)}
.post p{margin:24px auto 0;width:270px;text-align:center;font-size:12.5px;line-height:24px;color:#444}
.post .more{display:block;margin-top:10px;text-align:center;font-size:13px;font-weight:700;color:var(--blue);text-decoration:underline}

/* brands */
.brands{top:4130px;height:278px;background:var(--blue-bright)}
.brands h2{position:absolute;top:72px;width:100%;color:var(--white);font-size:33px}
.logo-box{position:absolute;top:142px;width:239px;height:77px;background:var(--white);display:flex;align-items:center;justify-content:center;font-size:26px;font-weight:700;color:#1a2a44}

/* footer */
.footer{position:absolute;left:0;top:4408px;width:1200px;height:361px;background:var(--footer);color:#e6e6e6}
.footer h4{position:absolute;top:64px;font-size:17px;font-weight:500;color:var(--white);text-transform:uppercase}
.links{position:absolute;top:97px;font-size:15px;line-height:32.5px}
.contact{position:absolute;left:463px;display:flex;align-items:center;gap:12px;font-size:15px;line-height:22px}
.contact .ic{width:32px;height:32px;border-radius:50%;background:#2a2a2a;display:flex;align-items:center;justify-content:center;flex:none}
.news-txt{position:absolute;left:770px;top:103px;width:330px;font-size:15px;line-height:24px}
.email{position:absolute;left:772px;top:151px;width:328px;height:43px;border-radius:22px;background:var(--white);color:#333;font-size:14px;padding:12px 16px}
.email .go{position:absolute;right:4px;top:4px;width:35px;height:35px;border-radius:50%;background:var(--blue-bright);display:flex;align-items:center;justify-content:center}
.social{position:absolute;top:213px;width:40px;height:40px;border-radius:50%;background:#2a2a2a}
.rule{position:absolute;left:100px;top:296px;width:1000px;border-top:1px solid #333}
.copy{position:absolute;top:312px;width:100%;text-align:center;font-size:14px}
</style>
</head>
<body>
<div class="page">

<section class="hero">
  <div class="hero-photo" role="img" aria-label="Speedboat moored at a wooden dock on a lake at sunset"></div>
  <div class="brand">HARBOR PEAK<br>MARINE &amp; AUTO</div>
  <div class="call">
    <span class="ico"><svg width="16" height="16" viewBox="0 0 24 24"><path fill="#fff" d="M6.6 10.8a15 15 0 0 0 6.6 6.6l2.2-2.2c.3-.3.7-.4 1-.2 1.1.4 2.3.6 3.6.6.6 0 1 .4 1 1V20c0 .6-.4 1-1 1A17 17 0 0 1 3 4c0-.6.4-1 1-1h3.5c.6 0 1 .4 1 1 0 1.3.2 2.5.6 3.6.1.3 0 .7-.2 1z"/></svg></span>
    <span><small>Call Us Today</small><strong>603 555 0188</strong></span>
  </div>
  <div class="search">Search here<svg width="16" height="16" viewBox="0 0 24 24"><circle cx="10" cy="10" r="7" fill="none" stroke="#333" stroke-width="2"/><path d="M15 15l6 6" stroke="#333" stroke-width="2"/></svg></div>
  <div class="btn book-top">Book an appointment</div>
  <nav class="nav">
    <span style="left:383px">HOME</span><span style="left:480px">ABOUT US</span><span style="left:604px">SERVICES</span><span style="left:724px">PRICING</span><span style="left:837px">BLOG</span><span style="left:926px">FAQ</span><span style="left:1006px">CONTACT US</span>
  </nav>
  <div class="hero-title">HARBOR PEAK</div>
  <div class="hero-sub-title">MARINE &amp; AUTO</div>
  <p class="hero-lead">We offer a broad range of boats and cars services in central New Hampshire</p>
  <div class="btn quote">Get a quote</div>
  <svg class="arrow" style="left:60px;top:300px" width="16" height="30" viewBox="0 0 16 30"><path d="M14 2L2 15l12 13" fill="none" stroke="#fff" stroke-width="2"/></svg>
  <svg class="arrow" style="left:1128px;top:300px" width="16" height="30" viewBox="0 0 16 30"><path d="M2 2l12 13L2 28" fill="none" stroke="#fff" stroke-width="2"/></svg>
  <div class="dots"><i></i><i class="on"></i><i></i><i></i></div>
</section>

<section class="mission">
  <h2 class="display center">Our Mission</h2>
  <p class="lead center">We aim to run a company focused on providing customers in the lakes region of the central New Hampshire with a broad range of premium boats and cars services.</p>
  <p class="body center">We are on a mission to support boat and car owners to keep their vessels and cars clean, well maintained, protected and safe wherever they are at convenient prices.</p>
</section>

<section class="services">
  <h2 class="display center">What We Do</h2>
  <svg class="arrow" style="left:66px;top:290px" width="14" height="26" viewBox="0 0 14 26"><path d="M12 2L2 13l10 11" fill="none" stroke="#333" stroke-width="2"/></svg>
  <svg class="arrow" style="left:1116px;top:290px" width="14" height="26" viewBox="0 0 14 26"><path d="M2 2l10 11L2 24" fill="none" stroke="#333" stroke-width="2"/></svg>

  <div class="svc" style="left:100px">
    <div class="ph" role="img" aria-label="Boat on a trailer covered in white shrink wrap" style="background:linear-gradient(180deg,#9fb7cf,#dfe6ee 55%,#7d8a70)"></div>
    <div class="badge"><svg width="28" height="28" viewBox="0 0 24 24" fill="none" stroke="#fff" stroke-width="1.6"><rect x="5" y="3" width="14" height="18" rx="2"/><path d="M8 8h8M8 12h8M8 16h5"/></svg></div>
    <h3>Boat for Shrink Wrapping</h3><div class="price">$19.00/per foot</div>
    <p>Lorem ipsum dolor sit amet, consectetur adipiscing elit, sed do eiusmod</p>
    <div class="book">BOOK NOW</div>
  </div>
  <div class="svc" style="left:352px">
    <div class="ph" role="img" aria-label="Detailer polishing the hull of a boat at a marina" style="background:linear-gradient(180deg,#7fb0d8,#e8eef3 60%,#b9c4cc)"></div>
    <div class="badge"><svg width="28" height="28" viewBox="0 0 24 24" fill="none" stroke="#fff" stroke-width="1.6"><circle cx="12" cy="12" r="8"/><circle cx="12" cy="12" r="3"/><path d="M12 2v4M12 18v4M2 12h4M18 12h4"/></svg></div>
    <h3>Boat Detailing</h3><div class="price">$23.00/per foot</div>
    <p>Lorem ipsum dolor sit amet, consectetur adipiscing elit, sed do eiusmod</p>
    <div class="book">BOOK NOW</div>
  </div>
  <div class="svc" style="left:604px">
    <div class="ph" role="img" aria-label="Boat covered in snow at winter storage" style="background:linear-gradient(180deg,#9a9a9a,#e9e9e9 50%,#5d5d5d)"></div>
    <div class="badge"><svg width="28" height="28" viewBox="0 0 24 24" fill="none" stroke="#fff" stroke-width="1.6"><path d="M12 2v20M3.3 7l17.4 10M3.3 17L20.7 7M9 4l3 3 3-3M9 20l3-3 3 3"/></svg></div>
    <h3>Boat Winterization Services</h3><div class="price">$200.00</div>
    <p>Lorem ipsum dolor sit amet, consectetur adipiscing elit, sed do eiusmod</p>
    <div class="book">BOOK NOW</div>
  </div>
  <div class="svc" style="left:856px">
    <div class="ph" role="img" aria-label="Car headlight being detailed in a dark garage" style="background:linear-gradient(135deg,#0f1a2e,#2b3b5c 50%,#6b4a4a)"></div>
    <div class="badge"><svg width="28" height="28" viewBox="0 0 24 24" fill="none" stroke="#fff" stroke-width="1.6"><path d="M3 15l2-6h14l2 6v4H3z"/><circle cx="7" cy="17" r="1.5"/><circle cx="17" cy="17" r="1.5"/></svg></div>
    <h3>Standard Auto Detailing</h3><div class="price">$180.00</div>
    <p>Lorem ipsum dolor sit amet, consectetur adipiscing elit, sed do eiusmod</p>
    <div class="book">BOOK NOW</div>
  </div>
</section>

<section class="stats" role="img" aria-label="Boat cutting through blue water, tinted blue">
  <h2 class="display center" style="color:#fff">The marine services market size will reach a value of more than $73.91 billion in 2021 and is expected to grow at a CAGR of 4.70% until 2028</h2>
  <div class="stat" style="left:119px"><div class="in">
    <svg width="72" height="60" viewBox="0 0 72 60" fill="none" stroke="#1A7FD0" stroke-width="2"><circle cx="36" cy="14" r="7"/><circle cx="18" cy="20" r="6"/><circle cx="54" cy="20" r="6"/><path d="M24 34c2-8 22-8 24 0M8 38c2-7 16-8 18-2M46 36c2-6 16-5 18 2M20 46l10-6h12l10 6-8 8H28z"/></svg>
    <div class="val">$73.91 B</div><div class="lbl">Marine services market size in 2021</div></div></div>
  <div class="stat" style="left:452px"><div class="in">
    <svg width="72" height="60" viewBox="0 0 72 60" fill="none" stroke="#1A7FD0" stroke-width="2"><circle cx="36" cy="14" r="7"/><circle cx="18" cy="20" r="6"/><circle cx="54" cy="20" r="6"/><path d="M24 34c2-8 22-8 24 0M8 38c2-7 16-8 18-2M46 36c2-6 16-5 18 2M20 46l10-6h12l10 6-8 8H28z"/></svg>
    <div class="val">+4.70%</div><div class="lbl">compounded annual growth until 2028</div></div></div>
  <div class="stat" style="left:785px"><div class="in">
    <svg width="72" height="60" viewBox="0 0 72 60" fill="none" stroke="#1A7FD0" stroke-width="2"><circle cx="36" cy="14" r="7"/><circle cx="18" cy="20" r="6"/><circle cx="54" cy="20" r="6"/><path d="M24 34c2-8 22-8 24 0M8 38c2-7 16-8 18-2M46 36c2-6 16-5 18 2M20 46l10-6h12l10 6-8 8H28z"/></svg>
    <div class="val">$101.98 B</div><div class="lbl">forecasted marine services market sizewithin the next seven years</div></div></div>
</section>

<section class="unique">
  <h2 class="center">Our uniqueness comes from our capability to provide customers with a first class experience and stress-free process featuring seamless access to a broad range of premium boat and car solutions from one provider</h2>
  <div class="big" style="left:96px;top:231px">S</div>
  <div class="big" style="left:604px;top:231px">W</div>
  <div class="big" style="left:96px;top:453px">O</div>
  <div class="big" style="left:604px;top:453px">T</div>

  <div class="sw" style="left:183px;top:218px">
    <div class="ic"><svg width="30" height="30" viewBox="0 0 24 24" fill="none" stroke="#1A7FD0" stroke-width="1.4"><circle cx="12" cy="7" r="3"/><circle cx="6" cy="10" r="2.4"/><circle cx="18" cy="10" r="2.4"/><path d="M7 19c1-5 9-5 10 0M2 20c0-4 6-5 7-3M15 17c1-2 7-1 7 3"/></svg></div>
    <h3>First class customer experience</h3>
    <p>We offer a wide array of services to make a better customer experience, including shrink wrapping, winterization, boat and car detailing and several regular maintenance services.</p>
  </div>
  <div class="sw" style="left:694px;top:218px">
    <div class="ic"><svg width="30" height="30" viewBox="0 0 24 24" fill="none" stroke="#1A7FD0" stroke-width="1.4"><rect x="5" y="9" width="14" height="11" rx="1"/><path d="M9 9V6h6v3M9 14h6"/></svg></div>
    <h3>Capital intensive</h3>
    <p>Our activity is capital intensive by definition and will require consistent upfront investment to develop a state-of-the-art operation and unfold the potential of our concept.</p>
  </div>
  <div class="sw" style="left:183px;top:453px">
    <div class="ic"><svg width="30" height="30" viewBox="0 0 24 24" fill="none" stroke="#1A7FD0" stroke-width="1.4"><path d="M3 20h18M6 17v-4M10 17V10M14 17v-6M18 17V6M5 11l5-4 4 3 5-5"/></svg></div>
    <h3>Growing markets</h3>
    <p>Big market potential with a solid and growing demand, with the opportunity to scale our growth and provide even more services without additional heavy investments required.</p>
  </div>
  <div class="sw" style="left:694px;top:453px">
    <div class="ic"><svg width="30" height="30" viewBox="0 0 24 24" fill="none" stroke="#1A7FD0" stroke-width="1.4"><circle cx="12" cy="12" r="4"/><path d="M12 3v3M12 18v3M3 12h3M18 12h3M5.6 5.6l2.1 2.1M16.3 16.3l2.1 2.1M5.6 18.4l2.1-2.1M16.3 7.7l2.1-2.1"/></svg></div>
    <h3>Negative externalities</h3>
    <p>Externalities reducing the volume of customers, including lower spending power due to economic recessions or new similar competitors could result in a longer payback period.</p>
  </div>
</section>

<section class="calendar">
  <div class="cal-band" role="img" aria-label="Blue-tinted water background"></div>
  <h2 class="display center" style="color:#fff">Calendar Booking</h2>
  <p class="intro center">Lorem ipsum dolor sit amet, consectetur adipiscing elit, sed do eiusmod tempor incididunt ut labore et dolore magna aliqua. Quis ipsum suspendisse ultrices gravida.</p>
  <div class="cal-card">
    <div class="cal-left">
      <div class="month">SEPTEMBER, 2021</div>
      <svg class="arrow" style="left:32px;top:189px" width="10" height="12" viewBox="0 0 10 12"><path d="M9 0v12L0 6z" fill="#222"/></svg>
      <svg class="arrow" style="left:545px;top:189px" width="10" height="12" viewBox="0 0 10 12"><path d="M1 0v12l9-6z" fill="#222"/></svg>
      <div class="grid">
        <span class="h">SUN</span><span class="h">MON</span><span class="h">TUE</span><span class="h">WED</span><span class="h">THUR</span><span class="h">FRI</span><span class="h">SAT</span>
        <span class="d">1</span><span class="d">2</span><span class="d">3</span><span class="d">4</span><span class="d">5</span><span class="d">6</span><span class="d on">7</span>
        <span class="d">8</span><span class="d on">9</span><span class="d">10</span><span class="d on">11</span><span class="d">12</span><span class="d">13</span><span class="d">14</span>
        <span class="d">15</span><span class="d">16</span><span class="d">17</span><span class="d">18</span><span class="d on">19</span><span class="d">20</span><span class="d">21</span>
        <span class="d">22</span><span class="d on">23</span><span class="d">24</span><span class="d">25</span><span class="d">26</span><span class="d">27</span><span class="d on">28</span>
        <span class="d">29</span><span class="d">30</span><span class="d">31</span>
      </div>
      <div class="btn sched">Schedule an appointment</div>
    </div>
    <div class="cal-brand">HARBOR PEAK<br>MARINE &amp; AUTO</div>
    <div class="event" style="top:148px"><div class="t"><b>09</b>FINIBUS BONORUM MRUM</div><p>Lorem ipsum dolor sit amet, cctetur aiscing elit, sed do ei Lorem ipsum dolor</p><hr></div>
    <div class="event" style="top:237px"><div class="t"><b>07</b>FINIBUS BONORUM MRUM</div><p>Lorem ipsum dolor sit amet, cctetur aiscing elit, sed do ei Lorem ipsum dolor</p><hr></div>
    <div class="event" style="top:326px"><div class="t"><b>23</b>FINIBUS BONORUM MRUM</div><p>Lorem ipsum dolor sit amet, cctetur aiscing elit, sed do ei Lorem ipsum dolor</p></div>
  </div>
</section>

<section class="news">
  <h2 class="display center">Latest News</h2>
  <article class="post" style="left:113px">
    <div class="ph" role="img" aria-label="White motor yacht on turquoise water under a blue sky" style="background:linear-gradient(180deg,#3f8fd6,#bfe0f4 55%,#3cc3cf)"></div>
    <div class="date" style="top:51px">05<small>SPE</small></div>
    <h3>Lorem ipsum dolor sit amet</h3>
    <p>Lorem ipsum dolor sit amet, cectetur adipiscing elit, sed do eiusmod tempor incididunt ut labore et dolore magna aliqua.</p>
    <span class="more">LEARN MORE »</span>
  </article>
  <article class="post" style="left:454px">
    <div class="ph" role="img" aria-label="Bow of a boat on open water under a pale sky" style="background:linear-gradient(180deg,#a9c3da,#d9e4ec 50%,#5a7c99)"></div>
    <div class="date" style="top:18px">05<small>SPE</small></div>
    <h3>Lorem ipsum dolor sit amet</h3>
    <p>Lorem ipsum dolor sit amet, cectetur adipiscing elit, sed do eiusmod tempor incididunt ut labore et dolore magna aliqua.</p>
    <span class="more">LEARN MORE »</span>
  </article>
  <article class="post" style="left:793px">
    <div class="ph" role="img" aria-label="Orange motorboat anchored in a calm bay" style="background:linear-gradient(180deg,#6aa9e0,#cfe3f2 45%,#2d6aa0 60%,#e07a2e 85%,#1f4f7a)"></div>
    <div class="date" style="top:18px">05<small>SPE</small></div>
    <h3>Lorem ipsum dolor sit amet</h3>
    <p>Lorem ipsum dolor sit amet, cectetur adipiscing elit, sed do eiusmod tempor incididunt ut labore et dolore magna aliqua.</p>
    <span class="more">LEARN MORE »</span>
  </article>
</section>

<section class="brands">
  <h2 class="display center" style="color:#fff">Our Brands</h2>
  <svg class="arrow" style="left:66px;top:168px" width="14" height="26" viewBox="0 0 14 26"><path d="M12 2L2 13l10 11" fill="none" stroke="#fff" stroke-width="2"/></svg>
  <svg class="arrow" style="left:1112px;top:168px" width="14" height="26" viewBox="0 0 14 26"><path d="M2 2l10 11L2 24" fill="none" stroke="#fff" stroke-width="2"/></svg>
  <div class="logo-box" style="left:100px">Halvenk</div>
  <div class="logo-box" style="left:354px">Trindle</div>
  <div class="logo-box" style="left:607px">Pike dorrel</div>
  <div class="logo-box" style="left:861px">Oro vane</div>
</section>

<footer class="footer">
  <h4 style="left:102px">Quick Links</h4>
  <div class="links" style="left:102px">Home<br>About Us<br>Services<br>Pricing<br>Blog<br>Contact Us</div>
  <h4 style="left:280px">Other Links</h4>
  <div class="links" style="left:280px">Privacy Policy<br>Terms of Service<br>Credit<br>FAQ</div>
  <h4 style="left:463px">Contact Us</h4>
  <div class="contact" style="top:100px"><span class="ic"><svg width="14" height="18" viewBox="0 0 24 30"><path fill="#fff" d="M12 0a10 10 0 0 0-10 10c0 8 10 20 10 20s10-12 10-20A10 10 0 0 0 12 0zm0 14a4 4 0 1 1 0-8 4 4 0 0 1 0 8z"/></svg></span><span>27 Weirs Cove Road<br>Laconia NH 03246</span></div>
  <div class="contact" style="top:154px"><span class="ic"><svg width="14" height="14" viewBox="0 0 24 24"><path fill="#fff" d="M6.6 10.8a15 15 0 0 0 6.6 6.6l2.2-2.2c.3-.3.7-.4 1-.2 1.1.4 2.3.6 3.6.6.6 0 1 .4 1 1V20c0 .6-.4 1-1 1A17 17 0 0 1 3 4c0-.6.4-1 1-1h3.5c.6 0 1 .4 1 1 0 1.3.2 2.5.6 3.6.1.3 0 .7-.2 1z"/></svg></span><span>603-555-0142</span></div>
  <div class="contact" style="top:204px"><span class="ic"><svg width="14" height="12" viewBox="0 0 24 18"><rect x="1" y="1" width="22" height="16" rx="2" fill="none" stroke="#fff" stroke-width="2"/><path d="M1 2l11 8 11-8" fill="none" stroke="#fff" stroke-width="2"/></svg></span><span>info@harborpeakmarine.com</span></div>
  <h4 style="left:770px">Keep Updated</h4>
  <p class="news-txt">Lorem ipsum dolor sit amet, consecr adipiscing elit, sed do eiusmod tempor incididunt ut</p>
  <div class="email">Your Email<span class="go"><svg width="16" height="16" viewBox="0 0 24 24"><path fill="#fff" d="M2 11L22 2l-6 20-4-8z"/></svg></span></div>
  <span class="social" style="left:769px" aria-label="Social profile link"></span>
  <span class="social" style="left:815px" aria-label="Social profile link"></span>
  <span class="social" style="left:861px" aria-label="Social profile link"></span>
  <span class="social" style="left:910px" aria-label="Social profile link"></span>
  <div class="rule"></div>
  <div class="copy">Copyright © 2021 Harbor Peak Marine and Auto. All rights reserved.</div>
</footer>

</div>
</body>
</html>
```